Bellwether Recovery Brochure for a drug and alcohol addiction treatment center.

***Update #2***
For graphic highlights no intrusion into text and no fade into adjoining areas.Use modern clean white layout with grey and light orange color scheme. Use attached yoga photo and other photos. For cover try moving number and logo around, and also try with cover photo not full size. Also use larger text with bullet points in a couple spots. Also try with new attached cover photos.
***Update*** I have attached some new photos to clarify the design wanted. My client likes the size (but not design) of the brochure in the newly included photos. Note the measurements - when closed it is 6" wide x 7" tall. When fully open it is 18" long, 7" wide, with 2 folds. I apologize if my terminology below was confusing. Please confirm that your design reflects the desired layout, and please modify your design if it does not. Thanks!
Want a trifold brochure 6" wide x 7" height. Design is for a drug and alcohol addiction treatment center. We want clean, soft, contemporary with highlight colors orange and grey, with contemporary font. Maybe some soft curves on design - see this A4 design we like but not the colors:
http://quillstockmart.net/item/business-trifold-brochure-wave/7315920?s_phrase=trifold%20business%20brochure&s_rank=54
See company web site for style cues and some content you can use:
http://bellwetherrecovery.com/
You can use the attached photos and logo in the design. Try sun in hand photo on cover, or man on beach. Please do not use the words "The Bellwether Recovery Center" in verbiage or titles, for business reasons we want to use "Bellwether Recovery Center" with no "The" instead.
Please note that the logo has been updated. The new logo is attached below. Use bellwether rev2.png for logo.
Addiction treatment industry professionals; family and decision makers of addict; addict themselves.

```html
<!DOCTYPE html>
<html lang="en">
<head>
<meta charset="utf-8">
<title>Bellwether Recovery Center Trifold Brochure</title>
<link rel="stylesheet" href="https://fonts.googleapis.com/css2?family=Open+Sans:wght@300;400;600;700&display=swap">
<style>
  :root {
    --page: #f5f2ed;
    --white: #ffffff;
    --orange: #f28a22;
    --orange-deep: #ee6a24;
    --mist: #e4eaf0;
    --ink: #3a3a3a;
    --ink-soft: #5b5b5b;
    --logo-ink: #111111;
    --photo-garden-a: #8ea374;
    --photo-garden-b: #737870;
    --photo-sunset-a: #b27a3c;
    --photo-sunset-b: #6d5036;
    --photo-beach-a: #e3a445;
    --photo-beach-b: #b88c5c;
    --photo-room-a: #d8cebf;
    --photo-room-b: #94846f;
    --photo-session-a: #d2cec8;
    --photo-session-b: #a19d97;
  }
  * { box-sizing: border-box; margin: 0; padding: 0; }
  html, body { width: 1200px; height: 533px; overflow: hidden; }
  body {
    background: var(--page);
    font-family: "Open Sans", Arial, sans-serif;
    color: var(--ink);
    position: relative;
  }
  .spread {
    position: absolute;
    top: 152px;
    width: 585px;
    height: 228px;
    display: flex;
    background: var(--white);
    box-shadow: 0 2px 8px rgba(0,0,0,.15);
  }
  .spread--outside { left: 10px; }
  .spread--inside { left: 605px; }
  .panel {
    position: relative;
    width: 195px;
    height: 100%;
    overflow: hidden;
  }
  .photo { position: absolute; }

  /* brand name lockup */
  .brand {
    display: flex;
    align-items: center;
    gap: 5px;
    color: var(--logo-ink);
    font-weight: 700;
    text-transform: uppercase;
    line-height: 1.05;
  }
  .brand__dot {
    flex: none;
    border-radius: 50%;
    background: var(--logo-ink);
  }

  /* outside: back panel */
  .services {
    position: absolute;
    top: 0; left: 0; right: 0;
    height: 132px;
    background: var(--mist);
    display: flex;
    gap: 6px;
    padding: 7px 6px 8px;
  }
  .service-card {
    flex: 1;
    border: 1px solid var(--orange);
    border-radius: 6px;
    background: var(--white);
    padding: 3px 4px;
    overflow: hidden;
  }
  .service-card__title {
    color: var(--orange);
    font-weight: 600;
    font-size: 7px;
    text-align: center;
    line-height: 1.2;
    margin-bottom: 3px;
  }
  .service-card__text {
    font-size: 4.2px;
    line-height: 1.35;
    text-align: justify;
    color: var(--ink-soft);
  }
  .photo--garden {
    top: 132px; left: 0; right: 0; bottom: 0;
    background: linear-gradient(180deg, var(--photo-garden-a), var(--photo-garden-b));
  }

  /* outside: flap panel */
  .panel--flap { background: var(--orange); }
  .panel--flap .brand {
    position: absolute;
    top: 62px; left: 0; right: 0;
    justify-content: center;
    font-size: 11px;
  }
  .panel--flap .brand__dot { width: 12px; height: 12px; }
  .call-band {
    background: var(--orange-deep);
    color: var(--white);
    text-align: center;
    font-size: 6px;
    line-height: 1.5;
  }
  .call-band strong { font-weight: 700; font-size: 6.5px; display: block; }
  .panel--flap .call-band {
    position: absolute;
    left: 0; right: 0; bottom: 0;
    height: 70px;
    padding-top: 17px;
  }

  /* outside: cover */
  .photo--sunset {
    inset: 0;
    background: linear-gradient(180deg, var(--photo-sunset-a), var(--photo-sunset-b));
  }
  .cover-title {
    position: absolute;
    top: 36px; left: 30px;
    color: var(--white);
    text-transform: uppercase;
  }
  .cover-title__name {
    display: inline-block;
    border: 1px solid rgba(255,255,255,.8);
    padding: 2px 8px;
    font-weight: 300;
    font-size: 18px;
    letter-spacing: .5px;
  }
  .cover-title__sub {
    font-weight: 300;
    font-size: 8.5px;
    letter-spacing: 1px;
    margin-top: 2px;
    padding-left: 9px;
  }

  /* inside: left panel */
  .photo--beach {
    inset: 0;
    background: linear-gradient(180deg, var(--photo-beach-a), var(--photo-beach-b));
  }
  .panel--welcome .brand {
    position: absolute;
    top: 12px; right: 10px;
    font-size: 7px;
  }
  .panel--welcome .brand__dot { width: 8px; height: 8px; }

  /* inside: middle panel */
  .panel--about .call-band {
    position: absolute;
    top: 0; left: 0; right: 0;
    height: 46px;
    background: var(--orange);
    padding-top: 12px;
  }
  .about-copy {
    position: absolute;
    top: 46px; left: 0; bottom: 0;
    width: 112px;
    background: var(--mist);
    padding: 40px 11px 0 24px;
    font-size: 4.6px;
    line-height: 1.45;
    text-align: justify;
  }
  .accent-block {
    position: absolute;
    top: 46px; left: 112px; right: 0;
    height: 46px;
    background: var(--orange-deep);
  }
  .photo--session {
    top: 104px; left: 108px; right: 0;
    height: 92px;
    background: linear-gradient(180deg, var(--photo-session-a), var(--photo-session-b));
  }

  /* inside: right panel */
  .photo--lounge {
    top: 0; left: 0; right: 0;
    height: 108px;
    background: linear-gradient(180deg, var(--photo-room-a), var(--photo-room-b));
  }
  .program-copy {
    position: absolute;
    top: 118px; left: 12px; right: 10px;
    font-size: 4.6px;
    line-height: 1.45;
    text-align: justify;
  }
  .program-copy p + p { margin-top: 5px; }
</style>
</head>
<body>

  <section class="spread spread--outside" aria-label="Brochure outside">
    <div class="panel panel--back">
      <div class="services">
        <article class="service-card">
          <h3 class="service-card__title">Alcohol Rehab</h3>
          <p class="service-card__text">Bellwether Recovery Center offers a contemporary approach to recovery from alcoholism. We recognize the necessity of treating the underlying issues from a psychological perspective, combining this with time-tested methods such as 12 step programs, and creating a synergy between these with a holistic approach to the individual.</p>
        </article>
        <article class="service-card">
          <h3 class="service-card__title">Drug Addiction Rehab</h3>
          <p class="service-card__text">At Bellwether Recovery Center we specialize in treatment of addiction for the entire spectrum of drugs that are abused in our contemporary society. Our nationally renowned clinical team has experience with treating addiction to all types of substances, while at the same time recognizing the unique nature of each individual client.</p>
        </article>
      </div>
      <div class="photo photo--garden" role="img" aria-label="Photo of a garden courtyard with a stone fountain, bench and trees"></div>
    </div>

    <div class="panel panel--flap">
      <div class="brand"><span class="brand__dot"></span><span>Bellwether<br>Recovery Center</span></div>
      <div class="call-band">Recover from Addiction<strong>Call 855-555-0142 Now</strong></div>
    </div>

    <div class="panel panel--cover">
      <div class="photo photo--sunset" role="img" aria-label="Photo of an open hand holding the setting sun above the sea"></div>
      <div class="cover-title">
        <div class="cover-title__name">Bellwether</div>
        <div class="cover-title__sub">Recovery Center</div>
      </div>
    </div>
  </section>

  <section class="spread spread--inside" aria-label="Brochure inside">
    <div class="panel panel--welcome">
      <div class="photo photo--beach" role="img" aria-label="Photo of a person standing at the shoreline at sunset"></div>
      <div class="brand"><span class="brand__dot"></span><span>Bellwether<br>Recovery Center</span></div>
    </div>

    <div class="panel panel--about">
      <div class="call-band">Recover from Addiction<strong>Call 855-555-0142 Now</strong></div>
      <div class="about-copy">Bellwether Recovery Center offers affordable treatment for a wide variety of addictions. We address underlying psychological disorders and specialize in treatment for drug addiction and alcoholism. At Bellwether Recovery Center we feature a full spectrum of addiction treatment programs, from initial assessment and detox, to inpatient residential and intensive outpatient care, as well as transitional housing and sober living environments for extended care.</div>
      <div class="accent-block"></div>
      <div class="photo photo--session" role="img" aria-label="Photo of a counselor leading a group session"></div>
    </div>

    <div class="panel panel--programs">
      <div class="photo photo--lounge" role="img" aria-label="Photo of a bright group room with chairs arranged in a circle"></div>
      <div class="program-copy">
        <p>Our clinical team are committed to treating each client with respect and are receptive to each clients' individual needs. Our treatment programs are abstinence based. We provide a comprehensive slate of services, such as individual, group counseling, drug and alcohol educational groups, and an introduction to 12-step programs. We also offer a strong family support program, recognizing the special importance of family healing in the recovery process.</p>
        <p>At Bellwether Recovery Center we believe strongly in a holistic approach to recovery through treating the mind, body, and soul. To facilitate this holistic recovery perspective we promote a healthy diet for our clients, and physical fitness through visits to a nationally recognized gym. In addition, guided yoga and meditation, hiking trips in Southern California's beautiful natural areas, and trips to the area's world-famous beaches are available during a client's stay.</p>
      </div>
    </div>
  </section>

</body>
</html>
```